Harbor Sushi & Steak Dinner Menu

I'm looking for a MENU design with a particular feel. I want to have a base template made that I can then use for future alterations to the menu; ie I can go in and change out different entrees as the menu changes but the template will remain the same. (Ideally it would be in an Apple Pages format.). Also ideally - dinner menu will occupy 2 pages 8.5 x 11. The restaurant's name is Harbor. It is a MODERN steak house that will also feature Sushi, a Raw Bar, Exquisite Cocktails and a sophisticated nightlife crowd. I have attached our LOGO, a secondary logo that we will be featuring throughout the project including on the menu cover (the gold U). Finally - I have attached the content that we would like to see. AGAIN - I REITERATE: High end dining and lounge atmosphere. A couple of restaurants / menus that I love are Morvendel in NYC and Pellucid Steakhouse in Long Island NY. Please do not duplicate - just trying to offer some suggestions.

Requirements
Must have
• A sophisticated and elegant feel without being stuffy or old.

```html
<!DOCTYPE html>
<html lang="en">
<head>
<meta charset="utf-8">
<title>Harbor Sushi &amp; Steak — Dinner Menu</title>
<link href="https://fonts.googleapis.com/css2?family=Arimo:ital,wght@0,400;0,700;1,400&family=Special+Elite&display=swap" rel="stylesheet">
<style>
:root{
  --ink:#0c0c0c;
  --red:#c8313f;
  --gold:#c9a84c;
  --cream:#ede3c3;
  --paper:#ffffff;
  --backdrop:#efefed;
  --text:#1a1a1a;
}
*{box-sizing:border-box;margin:0;padding:0}
html,body{width:1200px;height:800px;overflow:hidden;background:var(--backdrop)}
body{font-family:"Arimo",Arial,sans-serif;color:var(--text)}
.stage{position:absolute;left:0;top:0;width:1500px;height:1000px;transform:scale(.8);transform-origin:0 0}
.page{position:absolute;top:95px;width:630px;height:810px;background:var(--paper);box-shadow:0 2px 8px rgba(0,0,0,.12)}
.page--left{left:84px}
.page--right{left:771px}
.abs{position:absolute}
.masthead{left:30px;top:27px;width:571px;height:78px;background:var(--ink);display:flex;justify-content:center;align-items:center}
.masthead__brand{background:#151515;width:160px;height:78px;display:flex;align-items:center;justify-content:center;gap:8px;font-size:22px;letter-spacing:4px;color:var(--gold);font-weight:700}
.masthead__dot{width:7px;height:7px;border-radius:50%;background:var(--red)}
.footband{left:0;bottom:0;width:630px;height:20px;background:var(--ink)}
.box{border:1px solid #222;padding:14px 10px 8px;font-size:10px;line-height:14px}
.box::before{content:"";position:absolute;inset:3px;border:1px solid #222;pointer-events:none}
.box--red::before,.box--red{border-color:var(--red)}
.box--gold::before,.box--gold{border-color:var(--gold)}
.box-title{position:absolute;top:-9px;left:8px;background:var(--paper);padding:0 4px;color:var(--red);font-weight:700;font-size:14px;letter-spacing:.5px;line-height:16px;z-index:1}
.item b{font-weight:700}
.item i{font-style:italic}
.list .item{margin-bottom:0}
.menu-list .item{margin-bottom:4px;line-height:13px}
.special{left:234px;top:250px;width:367px;height:265px;background:var(--cream);padding:26px 12px 0 13px;font-size:10px;line-height:13px}
.special__title{font-family:"Special Elite",monospace;font-size:28px;text-align:center;margin-bottom:16px;color:var(--ink)}
.special .item{margin-bottom:5px;color:#333}
.special .item b{color:var(--ink)}
.art{position:absolute}
.rawbar{left:30px;top:537px;width:571px;height:50px;background:var(--ink);color:var(--cream);font-weight:700;font-size:24px;letter-spacing:.5px;padding:12px 18px}
.plain-list{font-size:12px;line-height:30px;padding:8px 8px}
.plate{font-size:10px;line-height:18px;padding:10px 12px}
.plate h3{font-size:14px;margin-bottom:2px}
.platters{left:234px;top:701px;width:367px;height:76px;background:var(--red);color:#fff;padding:10px 13px}
.platters h3{font-size:14px;letter-spacing:.4px}
.platters p{font-size:10px;margin-top:6px;color:#f3d6d9}
.platters strong{display:block;font-size:11px;margin-top:6px}
.steaks{left:32px;top:602px;width:365px;height:111px;background:var(--ink);color:#fff;display:flex;align-items:center}
.steaks__mark{width:180px;text-align:center}
.steaks__sub{font-size:13px;letter-spacing:1.5px;color:#ddd}
.steaks__word{font-family:"Special Elite",monospace;font-size:34px;color:var(--cream);line-height:38px}
.steaks__rule{width:66px;height:1px;background:var(--gold);margin:6px auto 0}
.steaks__list{list-style:none;font-size:10px;line-height:18px;font-weight:700;padding-left:8px}
.sides{font-size:10px;line-height:18px;padding:14px 14px 8px}
.sides .item{font-weight:700;line-height:14px;margin-bottom:4px}
.sauces{display:flex;font-size:10px;line-height:13px;padding:12px 6px 4px}
.sauces div{padding:0 6px;border-left:1px solid #444}
.sauces div:first-child{border-left:none}
.desserts{left:417px;top:732px;width:182px;height:43px;background:var(--red);color:#fff;padding:6px 12px}
.desserts::before{content:"";position:absolute;inset:3px;border:1px solid rgba(255,255,255,.5)}
.desserts h3{font-size:14px;letter-spacing:.5px}
.desserts p{font-size:11px}
</style>
</head>
<body>
<div class="stage">

  <!-- Sushi page -->
  <section class="page page--left">
    <header class="abs masthead"><div class="masthead__brand"><span class="masthead__dot"></span>HARBOR</div></header>

    <div class="abs box list" style="left:34px;top:127px;width:179px;height:148px">
      <h2 class="box-title">SUSHI / SASHIMI</h2>
      <p class="item"><b>Toro;</b> blue fin tuna belly (gf)</p>
      <p class="item"><b>Ebi;</b> cooked shrimp (gf)</p>
      <p class="item"><b>Hamachi;</b> yellowtail (gf)</p>
      <p class="item"><b>Uni;</b> sea urchin (gf)</p>
      <p class="item"><b>Hirame;</b> fluke (gf)</p>
      <p class="item"><b>Unagi;</b> fresh water eel (gf)</p>
      <p class="item"><b>Sake;</b> salmon (gf)</p>
      <p class="item"><b>Madai;</b> red snapper (gf)</p>
      <p class="item"><b>Maguro;</b> tuna (gf)</p>
    </div>

    <div class="abs box" style="left:234px;top:127px;width:367px;height:99px">
      <h2 class="box-title">SUSHI PLATTERS</h2>
      <p class="item"><b>SMALL</b></p>
      <p class="item">Five Pieces assorted sushi, nine pieces sashimi, spicy tuna roll (gf)</p>
      <p class="item" style="margin-top:5px"><b style="font-size:11px">LARGE</b></p>
      <p class="item">Eight Pieces assorted sushi, eighteen pieces of<br>sashimi, alaskan roll, rainbow roll (gf)</p>
    </div>

    <div class="abs box list" style="left:34px;top:301px;width:179px;height:200px">
      <h2 class="box-title">CLASSIC ROLLS</h2>
      <p class="item"><b>Yellowtail:</b> <i>inside out roll with scallions (gf)</i></p>
      <p class="item"><b>Spicy Tuna or Salmon or Yellowtail;</b> <i>spicy mayo</i></p>
      <p class="item"><b>California:</b> <i>crab meat, cucumber and avocado (gf)</i></p>
      <p class="item"><b>Vegetable:</b> <i>avocado, cucumber, asparagus and pickled reddish (gf)</i></p>
      <p class="item"><b>Spider:</b> <i>soft shell crab and avocado with eel sauce</i></p>
      <p class="item"><b>Shrimp Tempura:</b> <i>deep fried tempura shrimp and eel sauce</i></p>
      <p class="item"><b>Alaskan;</b> <i>salmon and avocado (gf)</i></p>
    </div>

    <div class="abs special">
      <h2 class="special__title">SPECIAL ROLLS</h2>
      <p class="item"><b>The Harbor:</b> <i>tuna, salmon, yellowtail, avocado, spicy mayo, soy bean paper</i></p>
      <p class="item"><b>King Crab Rainbow:</b> <i>king crab, avocado, cucumbers, assorted fish on top</i></p>
      <p class="item"><b>Empress:</b> <i>Shrimp tempura, spicy tuna on top, eel sauce, spicy mayo</i></p>
      <p class="item"><b>Spicy Girl:</b> <i>Spicy crunchy crab meat, cucumber, shrimp on top</i></p>
      <p class="item"><b>Dragon:</b> <i>Eel, cucumber, avocado, and tobiko on top, eel sauce</i></p>
      <p class="item"><b>Yummy:</b> <i>spicy crunchy salmon, avocado, mango and salmon on top</i></p>
      <p class="item"><b>No. 9:</b> <i>Shrimp Tempura, avocado, kani, spicy mayo, tobiko</i></p>
      <p class="item"><b>Sunrise Roll:</b> <i>spicy crunchy tuna and avocado,<br>spicy crunchy salmon on top</i></p>
      <div class="art" role="img" aria-label="Illustration of two sliced sushi rolls" style="right:2px;bottom:-8px;width:106px;height:58px;border-radius:29px;background:linear-gradient(90deg,#1a1a1a,#3a2a2a 50%,#c8313f)"></div>
    </div>

    <div class="abs rawbar">SEAFOOD RAW BAR
      <div class="art" role="img" aria-label="Illustration of a fish skeleton in gold and red" style="left:324px;top:6px;width:222px;height:56px;border-radius:28px;background:linear-gradient(90deg,#c9a84c 0%,#c9a84c 28%,#c8313f 40%,#c8313f 80%,#c9a84c 100%)"></div>
    </div>

    <div class="abs box plain-list" style="left:34px;top:605px;width:179px;height:170px">
      <p>Lobster Cocktail</p>
      <p>Shrimp Cocktail</p>
      <p>Clams on the Half Shell</p>
      <p>Oysters on the Half Shell</p>
      <p>Colossal Crab Cocktail</p>
    </div>

    <div class="abs box plate" style="left:234px;top:605px;width:365px;height:80px">
      <h3>Raw Bar Plate for One:</h3>
      <p>Two Shrimp, Half of a One Pound Lobster,<br>Two Clams, One East Coast Oyster, One West Coast Oyster</p>
    </div>

    <div class="abs platters">
      <h3>SEAFOOD PLATTERS</h3>
      <p>Shrimp, Oysters, Clams, Lobster and Crab</p>
      <strong>Large or Colossal</strong>
      <div class="art" role="img" aria-label="Line illustration of a crab" style="right:-2px;top:-2px;width:104px;height:80px;border-radius:50%;background:radial-gradient(circle,#d9545f,#a8222f)"></div>
    </div>

    <div class="abs footband"></div>
  </section>

  <!-- Steak page -->
  <section class="page page--right">
    <header class="abs masthead"><div class="masthead__brand"><span class="masthead__dot"></span>HARBOR</div></header>

    <div class="abs box menu-list" style="left:34px;top:127px;width:363px;height:171px">
      <h2 class="box-title">APPS</h2>
      <p class="item"><b>BAO Bun;</b> <i>hoisin bbq pancetta cut pork loin, crispy onions, micro mint</i></p>
      <p class="item"><b>Five Spice Crispy Popcorn Crusted Prawns (2);</b> <i>classic burre blanc</i></p>
      <p class="item"><b>Jumbo Lump Crab;</b> <i>citrus miso drizzle, spring pea puree, micro greens</i></p>
      <p class="item"><b>Crispy Wonton Napoleon;</b> <i>cucumber gallete, ahi tuna, jumbo lump crab meat, wasabi aioli, shoestring wontons</i></p>
      <p class="item"><b>PEI Mussels;</b> <i>charred artichoke hearts, blistered heirloom tomatoes, garlic white wine broth</i></p>
      <p class="item"><b>New Zealand or Domestic Small Eye Lamb Chop (1);</b> <i>crispy porcini risotto cake</i></p>
    </div>

    <div class="abs box menu-list" style="left:417px;top:127px;width:182px;height:331px">
      <h2 class="box-title">SALADS</h2>
      <p class="item"><b>Classic Wedge;</b><br><i>bleu cheese, bacon lardons, heirloom tomatoes</i></p>
      <p class="item"><b>Mixed Baby Greens;</b><br><i>heirloom tomatoes, cucumber, red onion, dijon vinaigrette</i></p>
      <p class="item"><b>Tabulleh;</b><br><i>buckwheat grain, fresh mint, tomato concasse, cucumber, parsley, fresh squeezed lemon, EVOO, salt and pepper</i></p>
      <p class="item"><b>Tomato Mozzarella Salad / Burratta</b></p>
      <p class="item"><b>Spinach Salad;</b><br><i>green apple, feta, currants, with per-simmons vinaigrette</i></p>
      <p class="item"><b>Kale Caesar;</b><br><i>homemade cacio e'peppe dress-ing, pecorino and parmesan cheese, toasted croutons.</i></p>
    </div>

    <div class="abs box box--red menu-list" style="left:34px;top:319px;width:363px;height:266px">
      <h2 class="box-title">ENTREES</h2>
      <p class="item"><b>Pan Roasted Miso Glazed Black Cod;</b> <i>green tea noodle stir fry; Napa cabbage, carrot, Japanese eggplant</i></p>
      <p class="item"><b>Pan Seared Striped Bass;</b> <i>lobster succotash in a tomato saffron broth</i></p>
      <p class="item"><b>E.V.O.O. Salted / Grilled Swordfish;</b> <i>sun dried tomato, olive and caper tapenade, over basmati rice</i></p>
      <p class="item"><b>Grilled Half Chicken;</b> <i>sun dried tomato and basil Israeli cous-cous, pan au jus</i></p>
      <p class="item"><b>Roasted Fresh Caviatelle Ratatoille;</b> <i>vegetable broth</i></p>
      <p class="item"><b>Lobster Cartoccio;</b> <i>shrimp, mussels, clams, fresh herb tomato broth, tossed with bucatini</i></p>
      <p class="item"><b>Charred Artichoke Hearts,</b> <i>heirloom tomatoes, caper berries, spring onions, fresh basil, white wine reduction over forbidden rice (gf)</i></p>
      <p class="item"><b>Mediterranean Grilled Veggie Plate;</b> <i>artichoke hearts, Japanese eggplant, green &amp; white asparagus, seared heirloom tomatoes, roasted baby carrots, cauliflower rice, evoo &amp; fig drizzle (gf)</i></p>
    </div>

    <div class="abs steaks">
      <div class="steaks__mark">
        <div class="steaks__sub">USDA PRIME</div>
        <div class="steaks__word">STEAKS</div>
        <div class="steaks__rule"></div>
      </div>
      <ul class="steaks__list">
        <li>10 Oz Filet</li>
        <li>14 or 16 oz New York Strip</li>
        <li>24 oz Boneless Ribeye</li>
        <li>36 oz Bone in Rib Eye</li>
        <li>Berkshire Pork Chop</li>
      </ul>
    </div>

    <div class="abs box box--gold sides" style="left:417px;top:481px;width:182px;height:232px">
      <h2 class="box-title">SIDES</h2>
      <p class="item">Mashed Idaho Potatoes</p>
      <p class="item">Bacon, Sweet Corn, Caramelized Vidalia Onion fingerling potatoes</p>
      <p class="item">Roasted Peanut Potatoes</p>
      <p class="item">Creamed Spinach</p>
      <p class="item">Sautéed Spinach</p>
      <p class="item">Grilled Asparagus</p>
      <p class="item">French Beans</p>
      <p class="item">Israeli Cous Cous</p>
      <p class="item">Sweet Potato Steak Fries</p>
      <p class="item">Corn Skillet</p>
    </div>

    <div class="abs box sauces" style="left:34px;top:733px;width:363px;height:44px">
      <h2 class="box-title">SOUCES</h2>
      <div>Cabernet Demi Glaz<br>Gorgonzola Brulle Cream</div>
      <div>Truffled Wild Mushroom<br>Ragu</div>
      <div>Horseradish Cream<br>House Steak Sauce</div>
    </div>

    <div class="abs desserts">
      <h3>DESSERTS</h3>
      <p>T.B.D. - separate menu</p>
    </div>

    <div class="abs footband"></div>
  </section>

</div>
</body>
</html>
```